Zerovan Medical

We are a medical supplier company we sell machines and equipment to all medical sectors in Iraq. Our services include not only the installation of these machines and equipment but also we provide support after installation and we train the staff to use these machines/equipment
We need a website that will make us stand out from our competitors, something professional and catchy
Starting from the home page, before showing the home page we want the loading screen to have our logo animated in a nice way
Then we can proceed to creating the other pages which are
Projects
Services
Training
About
and Contact us
Attached below is our logo and the color blue that we hope to use in the theme of the website
**** In the home page we want to focus on our partners and services****

Target Market(s)

Medical Sector

Industry/Entity Type

Medical

Coding

Coded - Design and coding required

Number of Pages Required

5+ page

Colors
0054AA
0677BA
7BADD7
CADEEF
E8F1F8

Requirements
Must have
• Animation in loading screen or animation in home page
Nice to have
• Some sort of animation for our partners

```html
<!DOCTYPE html>
<html lang="en">
<head>
<meta charset="utf-8">
<title>Zerovan Medical</title>
<link href="https://fonts.googleapis.com/css2?family=Libre+Baskerville:wght@400;700&family=Poppins:wght@400;500;600;700&display=swap" rel="stylesheet">
<style>
:root{
  --blue-deep:#0054AA;
  --blue:#0677BA;
  --blue-mid:#7BADD7;
  --blue-light:#CADEEF;
  --blue-pale:#E8F1F8;
  --yellow:#F5B800;
  --cream:#FDF4DF;
  --navy:#0A2448;
  --ink:#1E2A3A;
  --muted:#5A6676;
  --white:#FFFFFF;
}
*{box-sizing:border-box;margin:0;padding:0}
html,body{width:1200px;height:4524px;overflow:hidden}
body{position:relative;background:var(--white);font-family:'Poppins',sans-serif;color:var(--ink)}
.abs{position:absolute}
.serif{font-family:'Libre Baskerville',serif}
.brand{display:flex;align-items:center;gap:10px;font-family:'Poppins',sans-serif;font-weight:700;font-size:26px;color:var(--white)}
.brand-mark{width:30px;height:30px;border:4px solid var(--white)}
/* hero */
.hero{left:0;top:0;width:1200px;height:720px;background:linear-gradient(180deg,#1565B8 0%,#4B93D2 40%,#CFE2F3 78%,#EEF5FB 100%)}
.nav{left:112px;top:24px;width:976px;height:48px;display:flex;align-items:center;justify-content:space-between}
.nav-links{display:flex;gap:34px;font-size:15px;color:var(--white)}
.nav-links .active{color:var(--yellow)}
.hero-title{left:0;width:1200px;top:140px;text-align:center;font-size:40px;font-weight:700;color:var(--white)}
.hero-sub{left:330px;width:540px;top:204px;text-align:center;font-size:13px;line-height:20px;color:#E3EEF9}
.btn-yellow{background:var(--yellow);color:var(--ink);font-size:13px;font-weight:600;border-radius:6px;padding:10px 22px}
.hero-btn{left:540px;top:276px}
.hero-media{left:230px;top:340px;width:740px;height:340px;border-radius:10px;background:linear-gradient(180deg,rgba(255,255,255,.35),rgba(180,205,230,.9))}
/* about */
.about-media{left:160px;top:784px;width:360px;height:276px;border-radius:8px;background:linear-gradient(135deg,#B7D3EC,#6E9FC9)}
.eyebrow{font-size:14px;color:var(--yellow);font-weight:500}
.about-eyebrow{left:588px;top:806px}
.about-title{left:588px;top:836px;font-size:27px;font-weight:700;color:var(--ink)}
.about-text{left:588px;top:890px;width:480px;font-size:13px;line-height:22px;color:var(--muted)}
.feature{display:flex;align-items:center;gap:12px;font-size:14px;font-weight:500;color:var(--ink)}
.feature svg{flex:none}
/* equipment */
.section-title{left:0;width:1200px;text-align:center;font-size:27px;font-weight:700;color:var(--ink)}
.equip-card{width:216px;height:208px;border-radius:14px;background:linear-gradient(160deg,var(--blue-light),#A9C9E6)}
.equip-label{width:216px;text-align:center;font-size:15px;font-weight:500}
.dots{left:572px;top:1552px;display:flex;gap:6px}
.dots span{width:8px;height:8px;border-radius:50%;background:var(--blue-mid)}
.dots span:first-child{background:var(--blue-deep)}
/* training */
.training-band{left:0;top:1580px;width:1200px;height:680px}
.training-title{left:112px;top:1720px;font-size:27px;font-weight:700}
.training-text{left:112px;top:1776px;width:470px;font-size:13px;line-height:22px;color:var(--muted)}
.btn-blue{background:var(--blue-deep);color:var(--white);font-size:13px;font-weight:600;border-radius:8px;padding:10px 22px}
.photo{border-radius:8px;background:linear-gradient(135deg,#7FA9CF,#2E5E8E)}
/* services */
.hex{width:304px;height:320px;clip-path:polygon(50% 0,100% 25%,100% 75%,50% 100%,0 75%,0 25%);background:var(--blue-pale);display:flex;flex-direction:column;align-items:center;padding-top:82px;text-align:center}
.hex-icon{width:52px;height:52px;border-radius:50%;background:var(--yellow);display:flex;align-items:center;justify-content:center;margin-bottom:14px}
.hex h3{font-size:15px;font-weight:600;margin-bottom:8px}
.hex p{font-size:12.5px;line-height:19px;color:var(--muted);width:200px}
.hex a{margin-top:8px;font-size:12px;font-weight:600;color:var(--blue-deep);text-decoration:none}
/* projects */
.project{width:296px;height:376px;border-radius:12px;background:var(--white);box-shadow:0 6px 24px rgba(10,36,72,.13);overflow:hidden}
.project-media{height:200px;margin:8px;border-radius:8px;background:linear-gradient(135deg,#9CC1E2,#3C73A8)}
.project h3{font-size:15px;font-weight:600;line-height:22px;padding:6px 20px 0}
.project p{font-size:12.5px;line-height:20px;color:var(--muted);padding:10px 20px 0}
/* contact */
.map{left:0;top:3700px;width:1200px;height:300px;background:linear-gradient(135deg,#E4E9EC,#CFDAE0)}
.footer{left:0;top:3990px;width:1200px;height:534px;background:var(--navy)}
.contact-card{left:112px;top:3872px;width:976px;height:256px;background:var(--white);border-radius:16px;box-shadow:0 10px 30px rgba(10,36,72,.18)}
.contact-title{left:0;top:34px;width:976px;text-align:center;font-size:24px;font-weight:700}
.field{height:42px;border:1px solid #C9D4E0;border-radius:6px;font-size:12px;color:#8A95A3;padding:0 14px;display:flex;align-items:center}
.footer-head{font-size:20px;font-weight:500;color:var(--white)}
.footer-list{list-style:none;font-size:14px;line-height:30px;color:#D5DEEA}
.footer-list .active{color:var(--yellow)}
.contact-item{display:flex;align-items:flex-start;gap:12px;font-size:14px;line-height:22px;color:#D5DEEA}
.dot-icon{width:22px;height:22px;border-radius:50%;background:var(--yellow);flex:none;display:flex;align-items:center;justify-content:center}
.social{width:28px;height:28px;border-radius:50%;border:1.5px solid var(--white)}
.copyright{left:0;top:4478px;width:1200px;text-align:center;font-size:13px;color:#D5DEEA}
</style>
</head>
<body>

<!-- Hero -->
<section class="abs hero">
  <nav class="abs nav" style="left:112px;top:24px">
    <div class="brand"><span class="brand-mark"></span>Zerovan Medical</div>
    <div class="nav-links">
      <span class="active">Home</span><span>About</span><span>Services</span><span>Training</span><span>Projects</span><span>Contact us</span>
    </div>
  </nav>
  <h1 class="abs hero-title serif">Medical personal protective equipment</h1>
  <p class="abs hero-sub">Ut enim ad minim veniam, quis nostrud exercitation ullamco laboris nisi ut aliquip ex ea commodo consequat.</p>
  <span class="abs btn-yellow hero-btn">Shop Now</span>
  <div class="abs hero-media" role="img" aria-label="Row of medical machines and devices on a reflective floor"></div>
</section>

<!-- About -->
<section>
  <div class="abs about-media" role="img" aria-label="Collage of hospital rooms with medical equipment"></div>
  <span class="abs eyebrow about-eyebrow">About Product</span>
  <h2 class="abs about-title serif">Finding the Best Fit Products for You</h2>
  <p class="abs about-text">Effective For Cough, Wheezing, Asthma, COPD, Bronchitis And Other Respiratory Tract disorders State of the art technology.</p>
  <div class="abs feature" style="left:588px;top:970px"><svg width="22" height="22" viewBox="0 0 22 22"><rect x="3" y="3" width="16" height="16" rx="3" fill="none" stroke="#0054AA" stroke-width="2"/></svg>Compact and Stylish</div>
  <div class="abs feature" style="left:588px;top:1020px"><svg width="22" height="22" viewBox="0 0 22 22"><circle cx="11" cy="11" r="8" fill="none" stroke="#0054AA" stroke-width="2"/><path d="M7 11l3 3 5-6" fill="none" stroke="#0054AA" stroke-width="2"/></svg>Economical Choice</div>
  <div class="abs feature" style="left:820px;top:970px"><svg width="22" height="22" viewBox="0 0 22 22"><path d="M4 18L11 4l7 14z" fill="none" stroke="#0054AA" stroke-width="2"/></svg>Active Venturi System</div>
  <div class="abs feature" style="left:820px;top:1012px;width:240px;line-height:20px"><svg width="22" height="22" viewBox="0 0 22 22"><path d="M3 11h16M13 5l6 6-6 6" fill="none" stroke="#0054AA" stroke-width="2"/></svg>Simplicity and Effective Delivery</div>
</section>

<!-- Equipment -->
<section>
  <h2 class="abs section-title serif" style="top:1214px">Medical Equipment We Have</h2>
  <div class="abs equip-card" style="left:112px;top:1272px" role="img" aria-label="Microscope"></div>
  <div class="abs equip-card" style="left:368px;top:1272px" role="img" aria-label="Oxygen machine"></div>
  <div class="abs equip-card" style="left:624px;top:1272px" role="img" aria-label="Medical monitor"></div>
  <div class="abs equip-card" style="left:876px;top:1272px" role="img" aria-label="Operating table"></div>
  <div class="abs equip-label" style="left:112px;top:1494px">Microscope</div>
  <div class="abs equip-label" style="left:368px;top:1494px">Oxygen Machine</div>
  <div class="abs equip-label" style="left:624px;top:1494px">Medical Monitors</div>
  <div class="abs equip-label" style="left:876px;top:1494px">Operating Table</div>
  <div class="abs dots"><span></span><span></span><span></span><span></span></div>
</section>

<!-- Training -->
<section>
  <svg class="abs training-band" viewBox="0 0 1200 680" preserveAspectRatio="none" aria-hidden="true">
    <path d="M0 60 Q600 -40 1200 60 L1200 620 Q600 700 0 620 Z" fill="#FDF4DF"/>
  </svg>
  <h2 class="abs training-title serif">Training &amp; Certification</h2>
  <p class="abs training-text">Lorem ipsum dolor sit amet consectetur. Porttitor diam elementum eu ut enim felis aliquet commodo mauris. A eu sed ullamcorper lobortis sit viverra duis gravida. Et ac mauris tincidunt aliquam pharetra. Pellentesque in dictum vel dictum velit faucibus. Gravida et sagittis sit tincidunt vel aliquet fermentum lobortis. Integer semper viverra duis posuere lacus in pulvinar malesuada. Ultricies congue non amet mi.</p>
  <span class="abs btn-blue" style="left:112px;top:2036px">Learn More</span>
  <div class="abs photo" style="left:652px;top:1740px;width:204px;height:256px" role="img" aria-label="Medical staff discussing around a tablet"></div>
  <div class="abs photo" style="left:872px;top:1740px;width:132px;height:152px" role="img" aria-label="Trainer with doctors"></div>
  <svg class="abs" style="left:1020px;top:1740px" width="68" height="68" aria-hidden="true"><path d="M0 0 A68 68 0 0 1 68 68 L0 68 Z" fill="#0677BA"/></svg>
  <svg class="abs" style="left:872px;top:1906px" width="60" height="60" aria-hidden="true"><path d="M60 60 A60 60 0 0 1 0 0 L60 0 Z" fill="#F5B800"/></svg>
  <div class="abs photo" style="left:946px;top:1826px;width:142px;height:174px" role="img" aria-label="Doctors in training session"></div>
</section>

<!-- Services -->
<section>
  <h2 class="abs section-title serif" style="top:2264px">The Best Quality Service You Can Get</h2>
  <div class="abs hex" style="left:112px;top:2336px">
    <div class="hex-icon"><svg width="24" height="24" viewBox="0 0 24 24"><rect x="4" y="6" width="16" height="12" rx="2" fill="none" stroke="#1E2A3A" stroke-width="2"/></svg></div>
    <h3>Buy Imaging Equipment</h3><p>Lorem ipsum dolor sit amet consectetur. Aliquam eu vitae.</p><a>View All &gt;&gt;</a>
  </div>
  <div class="abs hex" style="left:448px;top:2336px">
    <div class="hex-icon"><svg width="24" height="24" viewBox="0 0 24 24"><path d="M4 8l8-4 8 4-8 4z M7 10v5c3 2 7 2 10 0v-5" fill="none" stroke="#1E2A3A" stroke-width="2"/></svg></div>
    <h3>Training &amp; Certification</h3><p>Lorem ipsum dolor sit amet consectetur. Aliquam eu vitae.</p><a>View All &gt;&gt;</a>
  </div>
  <div class="abs hex" style="left:784px;top:2336px">
    <div class="hex-icon"><svg width="24" height="24" viewBox="0 0 24 24"><path d="M5 19L19 5M5 5l14 14" stroke="#1E2A3A" stroke-width="2"/></svg></div>
    <h3>Equipment Service</h3><p>Lorem ipsum dolor sit amet consectetur. Aliquam eu vitae.</p><a>View All &gt;&gt;</a>
  </div>
  <div class="abs hex" style="left:280px;top:2576px">
    <div class="hex-icon"><svg width="24" height="24" viewBox="0 0 24 24"><circle cx="12" cy="12" r="8" fill="none" stroke="#1E2A3A" stroke-width="2"/><path d="M12 7v5l3 2" fill="none" stroke="#1E2A3A" stroke-width="2"/></svg></div>
    <h3>Fast On Site Response Time</h3><p>Lorem ipsum dolor sit amet consectetur. Aliquam eu vitae.</p><a>View All &gt;&gt;</a>
  </div>
  <div class="abs hex" style="left:616px;top:2576px">
    <div class="hex-icon"><svg width="24" height="24" viewBox="0 0 24 24"><path d="M12 3l7 3v5c0 5-3 8-7 10-4-2-7-5-7-10V6z" fill="none" stroke="#1E2A3A" stroke-width="2"/></svg></div>
    <h3>Annual Service Warranty</h3><p>Lorem ipsum dolor sit amet consectetur. Aliquam eu vitae.</p><a>View All &gt;&gt;</a>
  </div>
</section>

<!-- Projects -->
<section>
  <h2 class="abs section-title serif" style="top:3122px">Our Recent Projects</h2>
  <article class="abs project" style="left:112px;top:3200px"><div class="project-media" role="img" aria-label="Worker delivering medical supply boxes"></div><h3>Lorem ipsum dolor sit amet consectetur. Egestas enim.</h3><p>Lorem ipsum dolor sit amet consectetur......</p></article>
  <article class="abs project" style="left:452px;top:3200px"><div class="project-media" role="img" aria-label="Technicians working in a laboratory"></div><h3>Lorem ipsum dolor sit amet consectetur. Egestas enim.</h3><p>Lorem ipsum dolor sit amet consectetur......</p></article>
  <article class="abs project" style="left:792px;top:3200px"><div class="project-media" role="img" aria-label="Medical team in a training room"></div><h3>Lorem ipsum dolor sit amet consectetur. Egestas enim.</h3><p>Lorem ipsum dolor sit amet consectetur......</p></article>
  <svg class="abs" style="left:560px;top:3608px" width="80" height="24" aria-hidden="true"><path d="M4 12h22M4 12l7-6M4 12l7 6" stroke="#1E2A3A" stroke-width="2" fill="none"/><path d="M54 12h22M76 12l-7-6M76 12l-7 6" stroke="#0054AA" stroke-width="2" fill="none"/></svg>
</section>

<!-- Map & contact -->
<div class="abs map" role="img" aria-label="City street map showing the office location"></div>
<footer class="abs footer"></footer>
<section class="abs contact-card">
  <h2 class="abs contact-title serif">Get In Touch</h2>
  <div class="abs field" style="left:40px;top:92px;width:288px">First Name</div>
  <div class="abs field" style="left:344px;top:92px;width:288px">Email</div>
  <div class="abs field" style="left:648px;top:92px;width:288px">Phone No.</div>
  <div class="abs field" style="left:40px;top:164px;width:288px">Type Of Service</div>
  <div class="abs field" style="left:344px;top:164px;width:288px">Message</div>
  <span class="abs btn-blue" style="left:648px;top:166px">Submit Now</span>
</section>

<!-- Footer content -->
<div class="abs brand" style="left:112px;top:4120px;font-size:30px"><span class="brand-mark"></span>Zerovan Medical</div>
<p class="abs" style="left:112px;top:4180px;width:330px;font-size:14px;line-height:22px;color:#D5DEEA">Lorem ipsum dolor sit amet consectetur. Nisl mauris mi nibh tincidunt tortor.</p>
<div class="abs" style="left:112px;top:4248px;display:flex;gap:12px"><span class="social"></span><span class="social"></span><span class="social"></span><span class="social"></span></div>
<h3 class="abs footer-head" style="left:564px;top:4100px">Quick Links</h3>
<ul class="abs footer-list" style="left:564px;top:4140px"><li class="active">Home</li><li>About</li><li>Services</li><li>Training</li><li>Projects</li><li>Contact us</li></ul>
<h3 class="abs footer-head" style="left:824px;top:4100px">Contact Us</h3>
<div class="abs contact-item" style="left:824px;top:4150px;width:260px"><span class="dot-icon"><svg width="12" height="12" viewBox="0 0 12 12"><path d="M6 1a3.5 3.5 0 0 1 3.5 3.5C9.5 7 6 11 6 11S2.5 7 2.5 4.5A3.5 3.5 0 0 1 6 1z" fill="#0A2448"/></svg></span>742 Harbor View Rd Suite 8, Baytown, FL 33100</div>
<div class="abs contact-item" style="left:824px;top:4222px"><span class="dot-icon"><svg width="12" height="12" viewBox="0 0 12 12"><path d="M2 1h3l1 3-2 1c1 2 2 3 3 3l1-2 3 1v3c-5 0-9-4-9-9z" fill="#0A2448"/></svg></span>305-555-0148</div>
<div class="abs contact-item" style="left:824px;top:4266px"><span class="dot-icon"><svg width="12" height="12" viewBox="0 0 12 12"><rect x="1" y="3" width="10" height="7" fill="none" stroke="#0A2448" stroke-width="1.5"/><path d="M1 3l5 4 5-4" fill="none" stroke="#0A2448" stroke-width="1.5"/></svg></span>info@zerovanmedical.com</div>
<div class="abs" style="left:112px;top:4454px;width:976px;height:1px;background:rgba(255,255,255,.2)"></div>
<p class="abs copyright">Copyright © 2024 Zerovan Medical by . All Right Reserved.</p>

</body>
</html>
```